Website design for dressage horse training business

Looking to develop a new website design for a dressage horse training website. We want to change from a single landing page to one with multiple pages.
You are free to use your creativity to design the main landing page. This is the only page you need to design at this point. I would encourage looking at other Dressage Training websites to get a feel for what is typically on them. A few websites are listed below although I think the design of them could be better.
Notes:
- Menu to include: Home, Services, News Room, Blog, About Us, Contact,
- FAQ section on main page
- Logo to remain the same - the logo attached is not the correct color so change to match existing color.
- Change 'Sponsors' to 'Partnerships' on main page
Here is the link to the current site:
https://lindenridgestables.com/
Example sites
https://www.crestwoodsporthorsesco.com/
https://corinnalavelledressage.com/
Target Market(s)
Older women with disposable income
Number of Pages Required
1 page
Look and feel
Each slider illustrates characteristics of the customer's brand and the style your logo design should communicate.

```html
<!DOCTYPE html>
<html lang="en">
<head>
<meta charset="utf-8">
<title>Linden Ridge Stables – Dressage &amp; Sport Horse</title>
<link href="https://fonts.googleapis.com/css2?family=Cinzel:wght@400;600&family=Raleway:wght@400;500;600&family=Tinos:wght@700&display=swap" rel="stylesheet">
<style>
:root{
  --red:#b3261e;
  --red-dark:#8f1d17;
  --beige:#efeee1;
  --ink:#2a2a2a;
  --muted:#4a4a4a;
  --tan:#c7a68a;
  --sage:#a9b5a7;
  --sage-dark:#5f6f5d;
  --rose:#c98a84;
  --badge-bg:#efefef;
  --badge-shape:#c9c9c9;
  --white:#ffffff;
}
*{box-sizing:border-box;margin:0;padding:0}
html,body{width:1200px;height:4422px;overflow:hidden}
body{position:relative;background:var(--white);font-family:"Raleway",sans-serif;color:var(--ink)}
.abs{position:absolute}
.serif-title{font-family:"Cinzel",serif;font-weight:400;letter-spacing:1px}
.body-text{font-size:11px;line-height:24px;color:var(--muted)}
.btn{position:absolute;display:flex;align-items:center;height:34px;border-radius:4px;background:var(--red);color:var(--white);font-size:11px;text-decoration:none;overflow:hidden}
.btn span{flex:1;padding-left:20px}
.btn i{width:34px;height:100%;display:flex;align-items:center;justify-content:center;border-left:1px solid rgba(255,255,255,.35)}
.btn.tan{background:var(--tan)}
.chev{width:9px;height:14px}

/* hero */
.hero{left:0;top:0;width:1200px;height:530px;background:radial-gradient(ellipse at 50% 40%,#6e4a34 0%,#3f2a1f 55%,#231813 100%)}
.hero-photo{left:0;top:0;width:1200px;height:530px}
.nav{top:54px;left:0;width:1200px;height:20px;font-size:11px;color:var(--white);letter-spacing:.3px}
.nav a{position:absolute;color:var(--white);text-decoration:none}
.brand{position:absolute;text-align:center;color:var(--white);font-family:"Cinzel",serif;font-weight:400}
.brand-nav{left:490px;top:-14px;width:220px;font-size:21px;line-height:26px;white-space:nowrap}
.brand-nav small{display:block;font-size:10px;letter-spacing:8px;line-height:14px}
.hero-title{left:0;width:1200px;top:186px;text-align:center;color:var(--white);font-family:"Cinzel",serif;font-size:41px;line-height:50px}
.hero-sub{left:0;width:1200px;top:292px;text-align:center;color:var(--white);font-size:15px;letter-spacing:5px}

/* about */
.about-title{left:149px;top:628px;font-size:34px}
.about-text{left:149px;top:680px;width:510px}
.about-photo{left:745px;top:594px;width:455px;height:398px;background:linear-gradient(160deg,#8a8f74,#6d5d4a 55%,#a59a86)}

/* training */
.training{left:0;top:1013px;width:1200px;height:927px;background:var(--beige)}
.section-title{left:0;width:1200px;text-align:center;font-size:34px}
.train-photo-1{left:0;top:1202px;width:601px;height:323px;background:linear-gradient(120deg,#b98a5c,#6b3d22 55%,#c49a6c)}
.train-photo-2{left:599px;top:1525px;width:601px;height:324px;background:linear-gradient(100deg,#c23a35 0%,#d8d2c6 35%,#8a5a3a 70%,#b9a58e)}
.sub-title{font-size:21px;color:var(--red)}

/* testimonials */
.testimonials{left:0;top:1940px;width:1200px;height:313px;background:linear-gradient(90deg,#a82219,#b82b20 50%,#a82219)}
.quote-text{left:200px;width:800px;top:2120px;text-align:center;color:var(--white);font-size:11px;line-height:29px}
.dot{width:15px;height:15px;border:1.5px solid var(--white);border-radius:50%}

/* faq */
.faq-q{left:149px;top:2316px;font-family:"Tinos",serif;font-weight:700;font-size:22px;line-height:34px;color:#1e1e1e}
.map{left:0;top:2466px;width:613px;height:204px;background:linear-gradient(135deg,#d9e6d6,#c9dbe3 50%,#d6e2cf)}
.addr{font-family:"Tinos",serif;font-weight:700;font-size:14px;line-height:24px;color:#1e1e1e}
.faq-item{position:absolute;height:41px;display:flex;align-items:center;border-radius:3px;background:var(--sage);color:var(--white);font-size:10.5px;white-space:nowrap;overflow:hidden}
.faq-item b{flex:none;width:41px;height:41px;display:flex;align-items:center;justify-content:center;background:var(--sage-dark);font-weight:500;font-size:17px;border-radius:3px 0 0 3px;margin-right:16px}
.faq-item.open{background:var(--rose)}
.faq-item.open b{background:var(--red-dark)}
.faq-answer{left:769px;top:2466px;width:300px;font-size:10.5px;line-height:21px;color:var(--muted)}

/* sale */
.sale{left:0;top:2816px;width:1200px;height:712px;background:var(--beige)}
.sale-photo{left:584px;top:2953px;width:468px;height:512px;background:linear-gradient(180deg,#dfe3d4,#6b4632 45%,#3a2418 75%,#7a8a5c)}
.sale-card{left:146px;top:3027px;width:589px;height:364px;background:var(--white);box-shadow:0 4px 22px rgba(0,0,0,.12);padding:44px 36px 0 38px}
.sale-card h3{font-size:24px;margin-bottom:12px}
.sale-card p{font-size:10.5px;line-height:28px;color:var(--muted)}

/* partnerships */
.partner-badge{width:182px;height:148px;background:var(--badge-bg);display:flex;align-items:center;justify-content:center}
.partner-badge div{width:64px;height:64px;background:var(--badge-shape)}
.partner-name{font-size:19px}
.partner-text{width:250px;font-size:10px;line-height:20px;color:var(--muted)}

/* footer */
.footer{left:0;top:4018px;width:1200px;height:369px;background:linear-gradient(90deg,#2a2422,#3a3230 50%,#2a2422)}
.footer-brand{left:180px;top:4090px;width:170px;font-size:38px;line-height:42px;text-align:left}
.footer-brand small{display:block;font-size:11px;letter-spacing:16px;line-height:16px;padding-left:36px}
.footer-text{color:var(--white);font-size:11px;line-height:28px}
.footer-head{font-family:"Cinzel",serif;color:var(--white);font-size:19px}
.footer-links{left:464px;top:4131px;color:var(--white);font-size:11px;line-height:24px;list-style:none}
.insta{width:118px;height:103px}
.social{width:17px;height:17px;background:#3b7fc4;border-radius:2px}
.copyright{left:0;top:4387px;width:1200px;height:35px;background:var(--red);color:var(--white);font-size:11px;display:flex;align-items:center;justify-content:center}
</style>
</head>
<body>

<!-- Hero -->
<section class="abs hero">
  <div class="abs hero-photo" role="img" aria-label="Herd of dark bay horses running toward the camera"></div>
  <nav class="abs nav">
    <a style="left:222px">HOME</a>
    <a style="left:307px">SERVICES</a>
    <a style="left:411px">NEWS ROOM</a>
    <div class="brand brand-nav">LINDEN RIDGE<small>STABLES</small></div>
    <a style="left:710px">BLOG</a>
    <a style="left:790px">ABOUT US</a>
    <a style="left:900px">CONTACT</a>
    <svg class="abs" style="left:966px;top:-4px" width="18" height="18" viewBox="0 0 18 18" fill="none" stroke="#fff" stroke-width="1.6"><circle cx="10.5" cy="7.5" r="5"/><line x1="7" y1="11" x2="2" y2="16"/></svg>
  </nav>
  <h1 class="abs hero-title">Central Iowa's Premier<br>Dressage and Sport Horse</h1>
  <p class="abs hero-sub">Located outside Cedar Hollow, Iowa</p>
  <a class="btn" style="left:460px;top:337px;width:136px"><span>Read More</span><i><svg class="chev" viewBox="0 0 9 14" fill="none" stroke="#fff" stroke-width="1.8"><polyline points="2,1 8,7 2,13"/></svg></i></a>
  <a class="btn tan" style="left:605px;top:337px;width:136px"><span style="padding-left:30px">Services</span><i><svg class="chev" viewBox="0 0 9 14" fill="none" stroke="#fff" stroke-width="1.8"><polyline points="2,1 8,7 2,13"/></svg></i></a>
</section>
<svg class="abs" style="left:0;top:440px" width="1200" height="100" viewBox="0 0 1200 100">
  <path d="M0,34 Q600,120 1200,18 L1200,100 L0,100 Z" fill="#fff"/>
  <path d="M0,34 Q600,120 1200,18" fill="none" stroke="#b3261e" stroke-width="5"/>
</svg>
<svg class="abs" style="left:412px;top:503px" width="54" height="54" viewBox="0 0 54 54">
  <circle cx="27" cy="27" r="25" fill="#fff" stroke="#eee" stroke-width="2"/>
  <circle cx="27" cy="27" r="18" fill="#b3261e"/>
</svg>

<!-- About -->
<svg class="abs" style="left:250px;top:590px" width="370" height="350" viewBox="0 0 370 350"><circle cx="185" cy="175" r="172" fill="#f8efec"/></svg>
<h2 class="abs serif-title about-title">About Us</h2>
<p class="abs body-text about-text">Clara Whitfield began her riding career at a young age. She went up through the ranks of Pony Club and with an emphasis and focus in eventing. During college, Clara worked for a small breeder starting young horses. Clara loves starting young horses including starting and guiding them in a correct and quiet way to help them flourish. Her training focuses on gymnastic training incorporating ground work/lunging/long lining, jumping, cavelletti and regular hacking and trail riding. Clara is a NDF Silver Medalist having competed through the FEI levels of it. A learner at heart,</p>
<a class="btn" style="left:149px;top:875px;width:136px"><span>Read More</span><i><svg class="chev" viewBox="0 0 9 14" fill="none" stroke="#fff" stroke-width="1.8"><polyline points="2,1 8,7 2,13"/></svg></i></a>
<div class="abs about-photo" role="img" aria-label="Rider in black jacket on a pinto horse beside a wooden barn"></div>

<!-- Training & Lessons -->
<section class="abs training"></section>
<h2 class="abs serif-title section-title" style="top:1088px">Training &amp; Lessons</h2>
<div class="abs train-photo-1" role="img" aria-label="Close-up of a horse with a white blaze working in an arena"></div>
<h3 class="abs serif-title sub-title" style="left:627px;top:1283px">1: Training</h3>
<p class="abs body-text" style="left:627px;top:1322px;width:440px">Linden Ridge Stables offers both full and half time training options with Clara Whitfield. There is much flexibility with both rides and/or lessons weekly in the training packages that can be customized to fit both the horse and the rider's needs.</p>
<a class="btn" style="left:627px;top:1408px;width:136px"><span>Read More</span><i><svg class="chev" viewBox="0 0 9 14" fill="none" stroke="#fff" stroke-width="1.8"><polyline points="2,1 8,7 2,13"/></svg></i></a>
<h3 class="abs serif-title sub-title" style="left:146px;top:1606px">2: Lessons</h3>
<p class="abs body-text" style="left:146px;top:1645px;width:430px">Lessons are available for all ages of riders. Clara thoroughly enjoys working with accomplished riders looking to succeed in the show ring, as well as riders just wanting to learn what dressage is about. Come join our incredible and</p>
<a class="btn" style="left:145px;top:1730px;width:136px"><span>Read More</span><i><svg class="chev" viewBox="0 0 9 14" fill="none" stroke="#fff" stroke-width="1.8"><polyline points="2,1 8,7 2,13"/></svg></i></a>
<div class="abs train-photo-2" role="img" aria-label="Rider on a chestnut horse turning around a barrel in an arena"></div>

<!-- Testimonials -->
<section class="abs testimonials" role="img" aria-label="Faint red-toned photo of a horse and rider behind the testimonials"></section>
<h2 class="abs serif-title section-title" style="top:1990px;color:#fff">Testimonials</h2>
<svg class="abs" style="left:582px;top:2068px" width="36" height="28" viewBox="0 0 36 28" fill="#fff"><path d="M2,28 C0,16 4,6 14,2 L15,6 C9,9 8,14 9,17 L15,17 L15,28 Z"/><path d="M21,28 C19,16 23,6 33,2 L34,6 C28,9 27,14 28,17 L34,17 L34,28 Z"/></svg>
<p class="abs quote-text">Nullam turpis nibh, ullamcorper non nulla sed, varius imperdiet libero. Fusce iaculis sem pretium efficitur bibendum. Vestibulum metus leo, consequat ac placerat et, pulvinar in mauris. Proin neque metus, eleifend ut interdum vitae</p>
<div class="abs dot" style="left:568px;top:2192px"></div>
<div class="abs dot" style="left:593px;top:2192px;background:#fff"></div>
<div class="abs dot" style="left:617px;top:2192px"></div>

<!-- FAQ -->
<h2 class="abs faq-q">Do you have any questions?<br>See us FAQ. If you don't find the answer<br>call to us or visit us.</h2>
<div class="abs map" role="img" aria-label="Road map of the Cedar Hollow area with the farm location marked"></div>
<p class="abs addr" style="left:173px;top:2706px">Cedar Hollow<br>Iowa, USA</p>
<p class="abs addr" style="left:320px;top:2718px">555-014-0188</p>
<div class="faq-item" style="left:672px;top:2345px;width:388px"><b>1</b>Ut pulvinar, nulla non aliquet mollis</div>
<div class="faq-item open" style="left:713px;top:2405px;width:387px"><b>2</b>Duis a mi velit. Pellentesque nunc orci, scelerisque</div>
<p class="abs faq-answer">Maecenas eget massa quis tortor aliquam tempus. Maecenas sit amet justo sollicitudin, posuere lorem quis, ultricies ante. Nulla feugiat sem vel placerat rutrum. Ut feugiat posuere tincidunt.</p>
<div class="faq-item" style="left:672px;top:2565px;width:388px"><b>3</b>Maecenas interdum libero quis tellus maximus imperdiet.</div>
<div class="faq-item" style="left:672px;top:2625px;width:388px"><b>4</b>Integer quis fermentum ligula, sed consequat libero.</div>
<div class="faq-item" style="left:672px;top:2688px;width:388px"><b>5</b>In dapibus dignissim dolor, volutpat scelerisque metus</div>

<!-- For Sale -->
<section class="abs sale"></section>
<svg class="abs" style="left:20px;top:2820px" width="360" height="360" viewBox="0 0 360 360"><circle cx="180" cy="180" r="175" fill="#e9e3d4" opacity=".7"/></svg>
<h2 class="abs serif-title section-title" style="top:2867px">For Sale</h2>
<div class="abs sale-photo" role="img" aria-label="Dark bay Hanoverian gelding in a bridle standing outdoors"></div>
<article class="abs sale-card">
  <h3 class="serif-title">Northern Resolve</h3>
  <p>Nordlicht's Strength, "Rory," (Nordlicht x Harbor Pilot) is a 2012, 16hh imported Hanoverian. Rory is an incredibly quiet and kind horse. He is ridden by both an amatuer and child rider. He loves to hack and is very quiet alone and with a group of horses. He has shown through first level with scores into the 70's at both training and first level. Rory is currently solidly schooling all of second level, as well as half passes and flying changes from third level. Rory has 3 very easy to ride gaits and it is easy for riders to sit his trot. Very quiet and well mannered on the ground with vet, farrier and clipping. He has lovely confirmation with a striking head. He is regularly admired at shows! Rory is very versatile and game and also loves to jump!</p>
</article>

<!-- Partnerships -->
<h2 class="abs serif-title section-title" style="top:3583px">Partnerships</h2>
<div class="abs partner-badge" style="left:141px;top:3688px" role="img" aria-label="Partner badge placeholder"><div></div></div>
<h3 class="abs serif-title partner-name" style="left:350px;top:3706px">Fairmont Saddlery</h3>
<p class="abs partner-text" style="left:350px;top:3744px">Fairmont Saddlery is constantly designing and researching saddles and riders to find the right blend of design and craftmanship to fit today's demands. Every saddle's detail is carefully checked to be sure the workmanship and quality is there.</p>
<a class="btn" style="left:350px;top:3892px;width:128px"><span>Read More</span><i><svg class="chev" viewBox="0 0 9 14" fill="none" stroke="#fff" stroke-width="1.8"><polyline points="2,1 8,7 2,13"/></svg></i></a>
<div class="abs partner-badge" style="left:615px;top:3688px" role="img" aria-label="Partner badge placeholder"><div></div></div>
<h3 class="abs serif-title partner-name" style="left:824px;top:3706px">Halvorsen's Saddlery</h3>
<p class="abs partner-text" style="left:824px;top:3744px">My goal is to provide the best possible fit for both horse and rider whether it is a saddle you already own, one you have on trial, or one that I carry. Being a Qualified Saddle Fitter by the Guild of Saddle Makers allows me to work with all saddle types and brands. In addition, I</p>
<a class="btn" style="left:824px;top:3892px;width:128px"><span>Read More</span><i><svg class="chev" viewBox="0 0 9 14" fill="none" stroke="#fff" stroke-width="1.8"><polyline points="2,1 8,7 2,13"/></svg></i></a>

<!-- Footer -->
<footer class="abs footer"></footer>
<div class="abs brand footer-brand">LINDEN<small>RIDGE</small></div>
<p class="abs footer-text" style="left:194px;top:4170px;width:230px">FEI rider and trainer, Clara Whitfield began her riding career at a young age.</p>
<svg class="abs" style="left:199px;top:4246px" width="16" height="16" viewBox="0 0 16 16" fill="#fff"><path d="M3,1 L6,1 L7,5 L5,6.5 C6,9 7,10 9.5,11 L11,9 L15,10 L15,13 C15,14 14,15 13,15 C6,15 1,10 1,3 C1,2 2,1 3,1 Z"/></svg>
<p class="abs footer-text" style="left:230px;top:4240px">555-014-0188</p>
<svg class="abs" style="left:201px;top:4274px" width="13" height="18" viewBox="0 0 13 18" fill="#fff"><path d="M6.5,0 C3,0 0,2.8 0,6.3 C0,11 6.5,18 6.5,18 C6.5,18 13,11 13,6.3 C13,2.8 10,0 6.5,0 Z M6.5,9 A2.6,2.6 0 1,1 6.5,3.8 A2.6,2.6 0 1,1 6.5,9 Z"/></svg>
<p class="abs footer-text" style="left:230px;top:4270px">Cedar Hollow Iowa, USA</p>
<div class="abs social" style="left:197px;top:4318px"></div>
<div class="abs social" style="left:221px;top:4318px"></div>
<div class="abs social" style="left:245px;top:4318px"></div>
<div class="abs social" style="left:269px;top:4318px"></div>
<h4 class="abs footer-head" style="left:450px;top:4080px">Useful Links</h4>
<ul class="abs footer-links">
  <li>Home</li><li>About Us</li><li>Stallions</li><li>Sales</li><li>Gallery</li><li>Video</li><li>Contact Us</li>
</ul>
<h4 class="abs footer-head" style="left:668px;top:4080px">Follow On Instagram</h4>
<div class="abs insta" style="left:668px;top:4128px;background:linear-gradient(135deg,#6a4a32,#b08a5c)" role="img" aria-label="Saddles in a tack room"></div>
<div class="abs insta" style="left:792px;top:4128px;background:linear-gradient(135deg,#4a4038,#9a8a78)" role="img" aria-label="Horse in a barn aisle"></div>
<div class="abs insta" style="left:916px;top:4128px;background:linear-gradient(135deg,#8fa07a,#3a3a3a)" role="img" aria-label="Rider on a dark horse outdoors"></div>
<div class="abs insta" style="left:668px;top:4236px;background:linear-gradient(135deg,#5e7a4a,#4a2e20)" role="img" aria-label="Bay horse in a green field"></div>
<div class="abs insta" style="left:792px;top:4236px;background:linear-gradient(135deg,#c2a07a,#6a4226)" role="img" aria-label="Rider and horse in an arena"></div>
<div class="abs insta" style="left:916px;top:4236px;background:linear-gradient(135deg,#d0d0c8,#5a4a3a)" role="img" aria-label="Dressage test in a white-fenced arena"></div>
<div class="abs copyright">© 2021 Linden Ridge Stables All Rights Reserved.</div>

</body>
</html>
```